Design of a chocolate packaging

In hand-lettering-style: "Thank you for your work - you are an important part of our team!" (in big letters - almost 2/3 of the whole place) "This chocolate is a lot, so you enter into a raffle and have a great chance of a Velora Kip and many more great winnings ... all the information is below www.tvk-sonnenkreis.de! Good luck !!! " (in small letters underneath) The place is: 7,3cm * 15,3cm (crosswise)

Script

```html
<!DOCTYPE html>
<html lang="de">
<head>
<meta charset="utf-8">
<title>Schokoladenverpackung – Danke</title>
<link rel="stylesheet" href="https://fonts.googleapis.com/css2?family=Montserrat:wght@700&family=Cormorant+Garamond:ital,wght@1,600&display=swap">
<style>
  :root {
    --page: #ffffff;
    --frame: #e3c2b0;
    --choc-deep: #3f1d16;
    --choc-mid: #5e2a20;
    --choc-warm: #7a3a26;
    --choc-glow: #8a4330;
    --cream: #ecd0c0;
    --cream-soft: rgba(236, 208, 192, 0.55);
    --shadow: #2c120c;
  }
  html, body {
    margin: 0;
    padding: 0;
    width: 1200px;
    height: 1000px;
    overflow: hidden;
    background: var(--page);
  }
  .canvas {
    position: relative;
    width: 1200px;
    height: 1000px;
  }
  .wrapper-frame {
    position: absolute;
    left: 194px;
    top: 306px;
    width: 812px;
    height: 388px;
    background: var(--frame);
  }
  .wrapper-panel {
    position: absolute;
    left: 10px;
    top: 10px;
    width: 792px;
    height: 368px;
    overflow: hidden;
    background:
      radial-gradient(ellipse 45% 60% at 55% 45%, var(--choc-glow) 0%, transparent 70%),
      linear-gradient(180deg, var(--choc-warm) 0%, var(--choc-mid) 55%, var(--choc-deep) 100%);
  }
  .drip-band {
    position: absolute;
    left: 0;
    top: 0;
    width: 792px;
    height: 210px;
    background: linear-gradient(180deg, var(--shadow) 0%, rgba(63, 29, 22, 0.7) 40%, rgba(63, 29, 22, 0) 100%);
  }
  .headline {
    position: absolute;
    left: 0;
    top: 30px;
    width: 792px;
    margin: 0;
    text-align: center;
    font-family: 'Montserrat', sans-serif;
    font-weight: 700;
    font-size: 45px;
    line-height: 61px;
    letter-spacing: -0.3px;
    text-transform: uppercase;
    color: var(--cream);
    text-shadow:
      0 0 3px var(--shadow),
      0 0 6px var(--shadow),
      2px 2px 4px var(--shadow);
  }
  .raffle-note {
    position: absolute;
    left: 0;
    top: 226px;
    width: 792px;
    margin: 0;
    text-align: center;
    font-family: 'Cormorant Garamond', serif;
    font-style: italic;
    font-weight: 600;
    font-size: 28px;
    line-height: 31px;
    color: var(--cream);
    text-shadow: 0 0 3px var(--shadow);
  }
  .brand-mark {
    position: absolute;
    left: 662px;
    top: 168px;
    display: flex;
    align-items: center;
    gap: 6px;
    font-family: 'Montserrat', sans-serif;
    font-weight: 700;
    font-size: 13px;
    line-height: 15px;
    color: var(--cream-soft);
  }
  .brand-dot {
    width: 18px;
    height: 18px;
    border-radius: 50%;
    border: 2px solid var(--cream-soft);
  }
</style>
</head>
<body>
<div class="canvas">
  <div class="wrapper-frame">
    <div class="wrapper-panel">
      <div class="drip-band" role="img" aria-label="Illustration: herabtropfende flüssige Schokolade"></div>
      <h1 class="headline">Danke für deine Arbeit.<br>Du bist ein wichtiger Teil<br>unseres Teams.</h1>
      <div class="brand-mark">
        <span class="brand-dot"></span>
        <span class="brand-name">Sonnenkreis<br>Akademie</span>
      </div>
      <p class="raffle-note">Diese Schokolade ist ein Los.<br>Du nimmst damit an einer Verlosung Teil<br>und hast großartige Chancen auf einen Velora Kip<br>und viele weitere tolle Gewinne.</p>
    </div>
  </div>
</div>
</body>
</html>
```